Fall for Display rack for Fall Plant program to be displayed in Yardwell Supply

Signage for retail plant promotion for fall. Should picture a front porch with fall plants and have our logo on the bottom and the yardwell supply logo. Could feature fall items like pumkins, cinnamon, gords and more. Should have promotional tital Fresh for Fall! Should have the following selling components as well - Natural Front Door Decor / Enjoy Warm & Cozy Color/ Generate Fall Fresh Air. All should look festive, fresh and have a white wood background. Sign will measure 3 to 4 foot tall by 22.2inches
Target Market(s)
Mass Market Retail - Garden
Industry/Entity Type
Home And Garden
Requirements
Nice to have
- Fall colors. Doesnt have to be exactly what was picked just needs to look like fall.

```html
<!DOCTYPE html>
<html lang="en">
<head>
<meta charset="utf-8">
<title>Fresh for Fall! Display Sign</title>
<link rel="stylesheet" href="https://fonts.googleapis.com/css2?family=Yellowtail&family=Playball&family=Montserrat:wght@500&display=swap">
<style>
  :root {
    --backdrop: #e9e6df;
    --wood-white: #f3f3f2;
    --wood-seam: #c9c9c9;
    --band-red: #e9464f;
    --band-orange: #f08444;
    --band-green: #9ccb38;
    --title-magenta: #c2156f;
    --title-red: #ee2f4a;
    --title-orange: #f26b22;
    --ink-white: #ffffff;
    --brand-green: #3f5a2e;
    --brand-orange: #f26a1f;
  }
  * { box-sizing: border-box; margin: 0; padding: 0; }
  html, body { width: 1200px; height: 2361px; overflow: hidden; }
  body { background: var(--backdrop); position: relative; }

  .sign {
    position: absolute; left: 81px; top: 50px;
    width: 1037px; height: 2261px;
    background: var(--wood-white);
    overflow: hidden;
    box-shadow: 0 14px 30px rgba(0,0,0,.25);
  }
  .wood-seams { position: absolute; inset: 0; width: 100%; height: 100%; }

  .header { position: absolute; left: 0; top: 0; width: 100%; height: 694px; }
  .plant-croton {
    position: absolute; left: 0; top: 0; width: 300px; height: 420px;
    background: radial-gradient(ellipse at 30% 35%, #8b9a2a 0%, #6f7a22 35%, #b66a1f 65%, rgba(243,243,242,0) 78%);
  }
  .plant-cordyline {
    position: absolute; right: 0; top: 0; width: 420px; height: 500px;
    background: radial-gradient(ellipse at 85% 20%, #4a1d25 0%, #7a1e3e 35%, #d0246f 55%, rgba(243,243,242,0) 75%);
  }
  .title {
    position: absolute; left: 0; top: 170px; width: 100%;
    font-family: "Yellowtail", cursive;
    font-weight: 400;
    font-size: 235px; line-height: 190px;
    text-align: center;
    background: linear-gradient(100deg, var(--title-magenta) 20%, var(--title-red) 50%, var(--title-orange) 80%);
    -webkit-background-clip: text; background-clip: text; color: transparent;
    filter: drop-shadow(4px 6px 4px rgba(0,0,0,.25));
    transform: rotate(-4deg);
  }
  .title .line-one { display: block; padding-left: 120px; }
  .title .line-two { display: block; padding-left: 20px; }

  .band {
    position: absolute; left: 0; width: 100%; height: 353px;
    display: flex; align-items: center; justify-content: center;
    font-family: "Playball", cursive;
    font-size: 104px; line-height: 142px;
    color: var(--ink-white); text-align: center;
    text-shadow: 3px 4px 5px rgba(0,0,0,.3);
    border-top: 3px solid var(--ink-white);
  }
  .band-red { top: 694px; background: var(--band-red); }
  .band-orange { top: 1047px; background: var(--band-orange); }
  .band-green { top: 1400px; background: var(--band-green); }

  .footer { position: absolute; left: 0; top: 1753px; width: 100%; height: 508px; border-top: 3px solid var(--ink-white); }
  .brand {
    position: absolute; display: flex; align-items: center; gap: 16px;
    font-family: "Montserrat", sans-serif; font-weight: 500;
    white-space: nowrap;
  }
  .brand-maker { left: 130px; top: 125px; color: var(--brand-green); font-size: 48px; line-height: 54px; }
  .brand-maker .mark { flex: none; width: 76px; height: 76px; background: var(--brand-green); }
  .brand-retailer { left: 650px; top: 120px; color: var(--brand-orange); font-size: 38px; line-height: 44px; }
  .brand-retailer .mark { flex: none; width: 80px; height: 80px; background: var(--brand-orange); }
  .fall-leaves {
    position: absolute; left: 0; bottom: 0; width: 100%; height: 270px;
    background: linear-gradient(180deg, rgba(243,243,242,0) 0%, #f4c21a 30%, #e98a1a 60%, #c8321f 100%);
  }
</style>
</head>
<body>
  <main class="sign">
    <svg class="wood-seams" viewBox="0 0 1037 2261" aria-hidden="true">
      <g stroke="var(--wood-seam)" stroke-width="3" opacity=".6">
        <line x1="0" y1="620" x2="620" y2="0"/>
        <line x1="60" y1="1050" x2="1037" y2="73"/>
        <line x1="0" y1="1560" x2="1037" y2="523"/>
        <line x1="100" y1="1900" x2="1037" y2="963"/>
        <line x1="0" y1="2250" x2="1037" y2="1213"/>
        <line x1="600" y1="2261" x2="1037" y2="1824"/>
      </g>
    </svg>

    <header class="header">
      <div class="plant-croton" role="img" aria-label="Croton plant leaves in green, yellow and orange"></div>
      <div class="plant-cordyline" role="img" aria-label="Dark red and pink cordyline leaves"></div>
      <h1 class="title"><span class="line-one">Fresh</span><span class="line-two">for Fall!</span></h1>
    </header>

    <section class="band band-red"><p>Natural Front<br>Door Decor</p></section>
    <section class="band band-orange"><p>Enjoy Warm &amp;<br>Cozy Color</p></section>
    <section class="band band-green"><p>Generate Fall<br>Fresh Air</p></section>

    <footer class="footer">
      <div class="brand brand-maker"><span class="mark"></span><span>VERDANT<br>WORKS</span></div>
      <div class="brand brand-retailer"><span class="mark"></span><span>YARDWELL<br>SUPPLY</span></div>
      <div class="fall-leaves" role="img" aria-label="Row of red, orange and yellow maple leaves"></div>
    </footer>
  </main>
</body>
</html>
```